Eye-catching Yellow Page Ad for Attorney's Office

We need a phone book advertisement for our law office. We practice workers' compensation law, and our clientele consists exclusively of individuals who have been injured on the job. The dimensions of the print ad will be 6" W X 4.54" H.

We've had our current ad for several years, and wanted to get a new one that has been designed by a professional. Being that it's an ad for a law firm, it needs to be professional looking, but we're hoping to have something that looks a little more modern and has eye-catching appeal. We like the text that is included in the ad, and we want to make sure our phone number is very visible. No real preference for color scheme.

I've attached a copy of our current ad. All the information included in there is accurate. Our office name is Thornbury & Lisle, PLLC. The ethical rules for attorney advertising require the PLLC to be included in the ad, but it can be smaller than the other text (see our current ad).

Target Market(s)

Our potential clients are injured workers looking for legal representation in their workers' compensation claim.

Industry/Entity Type

Attorney

Font styles to use
Serif
Sans Serif

Requirements
Must have
• Professional, but stands out from the crowd
Nice to have
• Clean modern design
Should not have
• We don't want it to be too crowded or over-worked.

```html
<!DOCTYPE html>
<html lang="en">
<head>
<meta charset="utf-8">
<title>Thornbury &amp; Lisle, PLLC – Workers' Compensation</title>
<link rel="stylesheet" href="https://fonts.googleapis.com/css2?family=Open+Sans:ital,wght@0,400;0,700;0,800;1,400;1,700;1,800&display=swap">
<style>
  :root {
    --sun: #f7d12e;
    --red: #e8141b;
    --ink: #111111;
    --paper: #ffffff;
    --photo-a: #8a6a3e;
    --photo-b: #c9a06a;
  }
  html, body { margin: 0; padding: 0; overflow: hidden; background: var(--paper); }
  .ad {
    position: relative;
    width: 1200px;
    height: 1000px;
    overflow: hidden;
    background: var(--paper);
    font-family: "Open Sans", sans-serif;
  }
  .ad-shapes { position: absolute; inset: 0; }
  .firm-name {
    position: absolute; left: 68px; top: 78px; margin: 0;
    font-size: 47px; font-weight: 700; color: var(--sun); letter-spacing: 0.8px;
    white-space: nowrap;
  }
  .firm-name sup { font-size: 15px; vertical-align: 28px; margin-left: 2px; }
  .services {
    position: absolute; left: 143px; top: 158px; margin: 0; padding: 0; list-style: none;
  }
  .services li {
    position: relative; padding-left: 27px; height: 34.7px;
    font-size: 22px; font-style: italic; color: var(--red); white-space: nowrap;
    letter-spacing: 1.5px;
  }
  .services li::before {
    content: ""; position: absolute; left: 0; top: 6px;
    width: 18px; height: 18px; border-radius: 50%; background: var(--red);
  }
  .team-photo {
    position: absolute; left: 692px; top: 78px; width: 465px; height: 427px;
    background: linear-gradient(135deg, var(--photo-a), var(--photo-b) 50%, var(--photo-a));
  }
  .caption {
    position: absolute; top: 514px; margin: 0;
    font-size: 15px; font-weight: 700; color: var(--ink); white-space: nowrap;
  }
  .caption-left { left: 733px; }
  .caption-right { left: 1012px; }
  .practice-area {
    position: absolute; left: 28px; top: 528px; margin: 0;
    font-size: 50px; font-weight: 800; font-style: italic; color: var(--ink); white-space: nowrap;
    letter-spacing: 1.3px;
  }
  .call-label {
    position: absolute; left: 133px; top: 640px; margin: 0; z-index: 2;
    font-size: 28px; font-weight: 700; color: var(--red); line-height: 1; white-space: nowrap;
  }
  .phone {
    position: absolute; left: 140px; top: 643px; margin: 0; z-index: 1;
    font-size: 132px; font-weight: 700; color: var(--paper); letter-spacing: 11px; line-height: 1;
    white-space: nowrap;
  }
  .address {
    position: absolute; left: 0; width: 1216px; top: 772px; margin: 0; text-align: center;
    font-size: 33px; font-weight: 700; color: var(--red); letter-spacing: 4.3px; white-space: nowrap;
  }
  .website {
    position: absolute; left: 0; width: 1210px; top: 812px; margin: 0; text-align: center;
    font-size: 48px; font-weight: 700; color: var(--paper); letter-spacing: 1.7px; white-space: nowrap;
  }
  .values {
    position: absolute; top: 874px; margin: 0;
    font-size: 32px; font-style: italic; color: var(--red); letter-spacing: 1.5px; white-space: nowrap;
  }
  .value-1 { left: 90px; }
  .value-2 { left: 503px; }
  .value-3 { left: 918px; }
</style>
</head>
<body>
<div class="ad">
  <svg class="ad-shapes" width="1200" height="1000" viewBox="0 0 1200 1000" aria-hidden="true">
    <path d="M40 528 Q325 318 610 528 Z" fill="var(--sun)"/>
    <rect x="15" y="592" width="1170" height="346" fill="var(--sun)"/>
    <rect x="880" y="530" width="305" height="80" fill="var(--sun)"/>
    <ellipse cx="900" cy="430" rx="330" ry="242" fill="var(--paper)"/>
    <circle cx="393" cy="899" r="10" fill="var(--red)"/>
    <circle cx="823" cy="899" r="10" fill="var(--red)"/>
  </svg>

  <h1 class="firm-name">Thornbury &amp; Lisle<sup>PLLC</sup></h1>
  <ul class="services">
    <li>Workplace Injuries Or Death</li>
    <li>Lost Wages</li>
    <li>Medical Expencses &amp; Treatment</li>
    <li>Hearing Loss Claims</li>
    <li>Pension Claims</li>
    <li>Disability Awards</li>
    <li>Return To Work Issues</li>
  </ul>

  <div class="team-photo" role="img" aria-label="Photo of the two attorneys standing in a law library, one holding an open book"></div>
  <p class="caption caption-left">Oren Thornbury</p>
  <p class="caption caption-right">Kara Lisle</p>

  <h2 class="practice-area">Workers' Compensation</h2>

  <p class="call-label">Call Us Now:</p>
  <p class="phone">360555-0147</p>
  <p class="address">214 W. Harbor Suite 410, Fairhaven</p>
  <p class="website">www.thornburylisle.com</p>

  <p class="values value-1">Professional</p>
  <p class="values value-2">Committed</p>
  <p class="values value-3">Effective</p>
</div>
</body>
</html>
```